Rainbow card

Looking for someone to design a card using rainbow theme and link 7 different promises of love to each color. The design will be used to either print a greeting card for valentines or flyer type layout to be framed.

Target Market(s)

Personal

Font styles to use
Script

Colors
eb1f27
f78f20
faee3e
9bcb3c
0655a3
6a429a
a64599

Requirements
Must have
• Rainbow
• The phrases to be included on each color are:
• red - I'll never leave you as long as you'll have me.
• orange - I'll never deny you my body.
• yellow - I'll never let you go to prison.
• green - I'll have a baby with you.
• blue - I'll marry you.
• Indigo - I'll always love you.
• Violet - I'll always stand by you and support you.
Nice to have
• Rainbow, love and loyalty significance

```html
<!DOCTYPE html>
<html lang="en">
<head>
<meta charset="utf-8">
<title>Rainbow Promises Card</title>
<link rel="stylesheet" href="https://fonts.googleapis.com/css2?family=Dancing+Script:wght@500;600&display=swap">
<style>
  :root {
    --red: #eb1f27;
    --orange: #f78f20;
    --yellow: #faee3e;
    --green: #9bcb3c;
    --blue: #0655a3;
    --indigo: #6a429a;
    --violet: #a64599;
    --bright-violet: #9a3cf0;
    --bright-blue: #2a55e0;
    --sky-top: #a7b47a;
    --sky-mid: #f6f09a;
    --sky-low: #f3f1b0;
    --sky-bottom: #66787f;
    --ink: #2b2a22;
    --paper: #ffffff;
    --leaf: #8fd84a;
    --leaf-light: #c9f07c;
    --bloom-yellow: #f5d63a;
    --bloom-white: #e8f3fb;
  }
  * { margin: 0; padding: 0; box-sizing: border-box; }
  html, body { width: 1200px; height: 953px; overflow: hidden; background: var(--paper); }
  .card {
    position: relative;
    width: 1200px;
    height: 953px;
    background: var(--paper);
  }
  .scene {
    position: absolute;
    left: 50px; top: 50px;
    width: 1100px; height: 853px;
    overflow: hidden;
    background: linear-gradient(180deg,
      var(--sky-top) 0%,
      #c2c684 20%,
      #eeeb93 40%,
      #f8d88a 47%,
      var(--sky-mid) 56%,
      var(--sky-low) 66%,
      #b9bd9a 80%,
      var(--sky-bottom) 100%);
    box-shadow: inset 0 0 14px 4px rgba(255,255,255,0.9);
  }
  .rainbow { position: absolute; left: 0; top: 0; }
  .art { position: absolute; border-radius: 45%; filter: blur(2px); opacity: 0.75; }
  .leaves-top-left {
    left: 20px; top: 5px; width: 340px; height: 235px;
    background: radial-gradient(ellipse at 45% 45%, var(--leaf-light) 0%, var(--leaf) 35%, rgba(143,216,74,0) 70%);
  }
  .leaves-top-right {
    left: 900px; top: 5px; width: 200px; height: 355px;
    background: radial-gradient(ellipse at 55% 50%, var(--leaf-light) 0%, var(--leaf) 35%, rgba(143,216,74,0) 70%);
  }
  .flowers-yellow {
    left: 50px; top: 530px; width: 180px; height: 320px;
    background: radial-gradient(ellipse at 50% 40%, var(--bloom-yellow) 0%, #9ed64a 40%, rgba(158,214,74,0) 72%);
  }
  .shrub-green {
    left: 785px; top: 715px; width: 150px; height: 125px;
    background: radial-gradient(ellipse at 50% 50%, var(--leaf-light) 0%, var(--leaf) 40%, rgba(143,216,74,0) 72%);
  }
  .flowers-white {
    left: 950px; top: 525px; width: 130px; height: 325px;
    background: radial-gradient(ellipse at 50% 45%, var(--bloom-white) 0%, #9fd86a 45%, rgba(159,216,106,0) 75%);
  }
  .ground-line {
    position: absolute; left: 150px; top: 824px; width: 950px;
    border-top: 2px dotted #6fd03a;
  }
  .promises {
    position: absolute; left: 290px; top: 420px;
    list-style: none;
    font-family: "Dancing Script", cursive;
    font-weight: 600;
    font-size: 33px;
    letter-spacing: 0.6px;
    line-height: 52px;
    -webkit-text-stroke: 0.7px var(--ink);
  }
  .promise--red { color: var(--red); }
  .promise--orange { color: var(--orange); }
  .promise--yellow { color: var(--yellow); }
  .promise--green { color: var(--green); }
  .promise--blue { color: var(--blue); }
  .promise--indigo { color: var(--indigo); }
  .promise--violet { color: var(--violet); }
</style>
</head>
<body>
<main class="card">
  <section class="scene">
    <svg class="rainbow" width="1100" height="853" viewBox="50 50 1100 853" aria-hidden="true">
      <defs>
        <filter id="soft-edge" x="-10%" y="-10%" width="120%" height="120%">
          <feGaussianBlur stdDeviation="5"/>
        </filter>
      </defs>
      <g fill="none" stroke-width="30" filter="url(#soft-edge)">
        <path d="M -122 720 A 722 525 0 0 1 1322 720" stroke="var(--red)"/>
        <path d="M -100 720 A 700 498 0 0 1 1300 720" stroke="var(--orange)"/>
        <path d="M -78 720 A 678 471 0 0 1 1278 720" stroke="var(--yellow)"/>
        <path d="M -56 720 A 656 445 0 0 1 1256 720" stroke="var(--green)"/>
        <path d="M -34 720 A 634 418 0 0 1 1234 720" stroke="var(--bright-blue)"/>
        <path d="M -12 720 A 612 392 0 0 1 1212 720" stroke="var(--indigo)"/>
        <path d="M 11 720 A 589 365 0 0 1 1189 720" stroke="var(--bright-violet)"/>
      </g>
    </svg>

    <div class="art leaves-top-left" role="img" aria-label="Green leafy branches hanging from the top left corner"></div>
    <div class="art leaves-top-right" role="img" aria-label="Green leafy branches reaching in from the top right corner"></div>
    <div class="art flowers-yellow" role="img" aria-label="Yellow wildflowers and grass stems"></div>
    <div class="art shrub-green" role="img" aria-label="Small feathery green shrub"></div>
    <div class="art flowers-white" role="img" aria-label="Tall stems of white bell flowers"></div>
    <div class="ground-line"></div>

    <ul class="promises">
      <li class="promise promise--red">I'll never leave you as long as you'll have me.</li>
      <li class="promise promise--orange">I'll never deny you my body.</li>
      <li class="promise promise--yellow">I'll never let you go to prison.</li>
      <li class="promise promise--green">I'll have a baby with you.</li>
      <li class="promise promise--blue">I'll marry you.</li>
      <li class="promise promise--indigo">I'll always love you.</li>
      <li class="promise promise--violet">I'll always stand by you and support you.</li>
    </ul>
  </section>
</main>
</body>
</html>
```